K7 Dynamics Stationery Design Project

We are looking to have stationary designs created for our company branding materials. We are looking for the following to be created.
1. Business Cards (front & back)
2. Letterhead
3. Envelopes #10
We are a new web design, development and marketing firm. Primary color scheme is desired to be blue/grey/white. This web start-up is owned and operated by individuals with 15+ years experience each in the industry so should not look as though it is a start-up by young/inexperienced individuals.
We build website & custom applications/software. In addition we provide the full spectrum of web marketing solutions including SEO, PPC, Social Media, Branding, Content Marketing and PR.
Please let us know if you have any questions. Looking forward to seeing all the amazing design ideas.
Attached is our logo.
Thanks!
Target Market(s)
Company will be nearly 100% business to business sales. Looking to work with companies that are already established, with a website, who want to take their website and/or online marketing efforts to the next level.
Industry/Entity Type
Marketing
Look and feel

```html
<!DOCTYPE html>
<html lang="en">
<head>
<meta charset="utf-8">
<title>K7 Dynamics Business Cards</title>
<link href="https://fonts.googleapis.com/css2?family=Jost:wght@400;500;700&display=swap" rel="stylesheet">
<style>
  :root {
    --stage: #d9dbde;
    --white: #ffffff;
    --ink: #1d1d1f;
    --card-dark: #151618;
    --card-dark-edge: #2a2b2e;
    --blue: #1a8fd6;
    --blue-light: #2bb0e8;
    --blue-deep: #1770b8;
    --grey-text: #333333;
    --rule: #9a9a9a;
  }
  * { margin: 0; padding: 0; box-sizing: border-box; }
  html, body { width: 1200px; height: 753px; overflow: hidden; }
  body {
    position: relative;
    background: var(--stage);
    font-family: "Jost", "Futura", sans-serif;
  }
  .card {
    position: absolute;
    overflow: hidden;
    box-shadow: 0 6px 14px rgba(0,0,0,0.35);
  }
  .card--front-light { left: 50px; top: 37px; width: 530px; height: 308px; background: var(--white); }
  .card--front-dark  { left: 622px; top: 42px; width: 526px; height: 306px; background: radial-gradient(ellipse at 40% 40%, var(--card-dark-edge), var(--card-dark) 70%); }
  .card--back-dark   { left: 55px; top: 408px; width: 525px; height: 300px; background: radial-gradient(ellipse at 50% 40%, var(--card-dark-edge), var(--card-dark) 70%); }
  .card--back-blue   { left: 632px; top: 408px; width: 525px; height: 300px; background: radial-gradient(ellipse at 50% 45%, var(--blue-light), var(--blue-deep) 80%); }

  .brand-dot {
    position: absolute;
    width: 64px; height: 64px;
    border-radius: 50%;
    background: var(--blue);
  }
  .card--back-blue .brand-dot { background: var(--white); }

  .brand-name {
    position: absolute;
    font-weight: 700;
    font-size: 28px;
    letter-spacing: 0.2px;
    white-space: nowrap;
    line-height: 1;
  }
  .tagline {
    position: absolute;
    font-size: 11px;
    font-weight: 500;
    white-space: nowrap;
  }
  .web {
    position: absolute;
    font-size: 17px;
    white-space: nowrap;
  }
  .divider {
    position: absolute;
    width: 1px;
    height: 125px;
    background: var(--rule);
  }
  .contact {
    position: absolute;
    font-size: 14px;
    line-height: 20px;
    list-style: none;
  }
  .contact li { display: flex; align-items: center; gap: 4px; white-space: nowrap; }
  .contact svg { width: 12px; height: 12px; flex: none; }
  .address {
    position: absolute;
    font-size: 14px;
    line-height: 18px;
  }
  .wave { position: absolute; left: 0; bottom: 0; width: 100%; height: 100%; }
  .person {
    position: absolute;
    color: var(--white);
    font-size: 17px;
    font-weight: 700;
    white-space: nowrap;
  }
  .person span { font-weight: 400; font-size: 15px; }

  .on-light { color: var(--ink); }
  .on-light .tagline, .on-light.contact, .on-light.address { color: var(--grey-text); }
  .on-dark { color: var(--white); }
</style>
</head>
<body>

<!-- Front, white -->
<section class="card card--front-light">
  <div class="brand-dot" style="left:118px; top:70px;"></div>
  <div class="brand-name on-light" style="left:45px; top:178px;">K7 DYNAMICS</div>
  <div class="tagline on-light" style="left:45px; top:202px; color:var(--grey-text);">Web Design, Development and Marketing</div>
  <div class="divider" style="left:294px; top:92px;"></div>
  <ul class="contact on-light" style="left:320px; top:94px; color:var(--grey-text);">
    <li><svg viewBox="0 0 12 12"><circle cx="6" cy="6" r="5.3" fill="none" stroke="var(--blue)" stroke-width="1.2"/><path d="M4 3.5l1 1.3-.6.7c.4.9 1 1.5 1.9 1.9l.7-.6 1.3 1-.6 1c-2.4-.3-4.3-2.2-4.6-4.6z" fill="var(--blue)"/></svg>123-456-7890</li>
    <li><svg viewBox="0 0 12 12"><rect x="1" y="3" width="10" height="7" fill="var(--blue)"/><path d="M1 3l5 4 5-4" fill="none" stroke="#fff" stroke-width="1"/></svg>info@k7dynamics.com</li>
    <li><svg viewBox="0 0 12 12"><circle cx="6" cy="6" r="5" fill="none" stroke="var(--blue)" stroke-width="1.2"/><path d="M1 6h10M6 1c-3 3-3 7 0 10M6 1c3 3 3 7 0 10" fill="none" stroke="var(--blue)" stroke-width="1"/></svg>www.k7dynamics.com</li>
  </ul>
  <div class="address" style="left:321px; top:180px; color:var(--grey-text);">Street Name, City Name<br>State Zip code</div>
  <svg class="wave" viewBox="0 0 530 308" preserveAspectRatio="none" aria-hidden="true">
    <path d="M0 272 C120 300 260 282 380 262 C450 250 500 255 530 268 L530 308 L0 308Z" fill="var(--card-dark)"/>
    <path d="M0 268 C120 296 260 276 380 256 C450 244 500 250 530 266 L530 272 C500 258 450 254 380 266 C260 286 120 304 0 276Z" fill="var(--blue)"/>
  </svg>
  <div class="person" style="left:336px; top:270px;">Your Name, <span>Title</span></div>
</section>

<!-- Front, dark -->
<section class="card card--front-dark">
  <div class="brand-dot" style="left:112px; top:70px;"></div>
  <div class="brand-name on-dark" style="left:43px; top:175px;">K7 DYNAMICS</div>
  <div class="tagline on-dark" style="left:43px; top:199px;">Web Design, Development and Marketing</div>
  <div class="divider" style="left:290px; top:92px; background:#777;"></div>
  <ul class="contact on-dark" style="left:318px; top:93px;">
    <li><svg viewBox="0 0 12 12"><circle cx="6" cy="6" r="5.3" fill="none" stroke="#fff" stroke-width="1.2"/><path d="M4 3.5l1 1.3-.6.7c.4.9 1 1.5 1.9 1.9l.7-.6 1.3 1-.6 1c-2.4-.3-4.3-2.2-4.6-4.6z" fill="#fff"/></svg>123-456-7890</li>
    <li><svg viewBox="0 0 12 12"><rect x="1" y="3" width="10" height="7" fill="#fff"/><path d="M1 3l5 4 5-4" fill="none" stroke="var(--card-dark)" stroke-width="1"/></svg>info@k7dynamics.com</li>
    <li><svg viewBox="0 0 12 12"><circle cx="6" cy="6" r="5" fill="none" stroke="#fff" stroke-width="1.2"/><path d="M1 6h10M6 1c-3 3-3 7 0 10M6 1c3 3 3 7 0 10" fill="none" stroke="#fff" stroke-width="1"/></svg>www.k7dynamics.com</li>
  </ul>
  <div class="address on-dark" style="left:319px; top:177px;">Street Name, City Name<br>State Zip code</div>
  <svg class="wave" viewBox="0 0 526 306" preserveAspectRatio="none" aria-hidden="true">
    <path d="M0 262 C120 292 260 276 380 254 C450 242 500 248 526 262 L526 306 L0 306Z" fill="var(--white)"/>
    <path d="M0 270 C120 300 260 284 380 262 C450 250 500 256 526 270 L526 306 L0 306Z" fill="#000"/>
    <path d="M0 276 C120 304 260 290 380 268 C450 256 500 262 526 276 L526 306 L0 306Z" fill="var(--blue)"/>
  </svg>
  <div class="person" style="left:334px; top:268px;">Your Name, <span>Title</span></div>
</section>

<!-- Back, dark -->
<section class="card card--back-dark">
  <div class="brand-dot" style="left:230px; top:64px;"></div>
  <div class="brand-name on-dark" style="left:140px; top:198px; font-size:30px;">K7 DYNAMICS</div>
  <div class="tagline on-dark" style="left:141px; top:230px; font-size:12px;">Web Design, Development and Marketing</div>
  <div class="web on-dark" style="left:167px; top:250px;">www.k7dynamics.com</div>
</section>

<!-- Back, blue -->
<section class="card card--back-blue">
  <div class="brand-dot" style="left:230px; top:64px;"></div>
  <div class="brand-name on-dark" style="left:140px; top:195px; font-size:30px;">K7 DYNAMICS</div>
  <div class="tagline on-dark" style="left:141px; top:226px; font-size:12px;">Web Design, Development and Marketing</div>
  <div class="web on-dark" style="left:167px; top:246px;">www.k7dynamics.com</div>
</section>

</body>
</html>
```